modernized upgrade to existing squarespace site

Hello! I have the following page for my consulting firm: https://hollinbrookcounsel.com/ Would love to upgrade to something more modern/attractive like here: https://www.pemberlowgroup.com/ or https://brightquillstudio.com/ , but I am open to creativity. Would like to retain the logo look and color theme from the logo. The rest can be left to creative discretion.

```html
<!DOCTYPE html>
<html lang="en">
<head>
<meta charset="utf-8">
<title>Hollinbrook Counsel</title>
<link rel="stylesheet" href="https://fonts.googleapis.com/css2?family=Cormorant+Garamond:wght@500;600;700&family=Noto+Sans:wght@400;500&display=swap">
<style>
:root{
  --rose:#c4877e;
  --rose-soft:#d4a49c;
  --ink:#111;
  --body:#333;
  --white:#fff;
  --hero-a:#3e3a38;
  --hero-b:#6b625c;
  --cta:#5d5e61;
  --serif:'Cormorant Garamond', Georgia, serif;
  --sans:'Noto Sans', Arial, sans-serif;
}
*{margin:0;padding:0;box-sizing:border-box}
html,body{width:1200px;height:3926px;overflow:hidden;background:var(--white)}
body{position:relative;font-family:var(--sans);color:var(--body)}
a{text-decoration:none}
.btn{position:absolute;display:flex;align-items:center;justify-content:center;background:var(--rose);color:var(--white);font-family:var(--serif);font-weight:700;font-size:18px}
.photo{position:absolute}

/* hero */
.hero{position:absolute;left:0;top:0;width:1200px;height:605px;background:linear-gradient(160deg,#4a4542 0%,var(--hero-a) 45%,var(--hero-b) 100%)}
.hero-shade{position:absolute;inset:0;background:linear-gradient(90deg,rgba(20,18,17,.55),rgba(20,18,17,.15))}
.brand{position:absolute;left:110px;top:18px;display:flex;align-items:center;gap:14px;color:var(--white)}
.brand-mark{width:60px;height:58px;border:2px solid var(--white)}
.brand-name{font-family:var(--serif);font-weight:500;font-size:24px;letter-spacing:2px;line-height:26px;text-transform:uppercase;width:210px}
.nav{position:absolute;left:405px;top:32px;display:flex;gap:22px;font-family:var(--serif);font-weight:600;font-size:18px}
.nav a{color:var(--white)}
.nav a.active{text-decoration:underline;text-underline-offset:5px}
.hero h1{position:absolute;left:108px;top:160px;width:600px;font-family:var(--serif);font-weight:600;font-size:55px;line-height:56px;color:var(--white)}
.hero p{position:absolute;left:109px;top:338px;width:430px;font-size:14px;line-height:32px;color:var(--white)}

/* generic */
.title{position:absolute;left:0;width:1200px;text-align:center;font-family:var(--serif);font-weight:600;font-size:45px;color:var(--ink)}
.center-copy{position:absolute;left:160px;width:880px;text-align:center;font-size:15px;line-height:32px}
.feature h2{position:absolute;font-family:var(--serif);font-weight:600;font-size:44px;line-height:48px;color:var(--ink)}
.feature p{position:absolute;font-size:14px;line-height:30.2px}
.feature .mail{position:absolute;font-size:18px;font-weight:500;color:var(--rose)}

/* services */
.services{position:absolute;left:0;top:2170px;width:1200px;height:483px;background:var(--rose)}
.services .title{color:var(--white);top:64px}
.service{position:absolute;top:160px;width:300px;text-align:center;color:var(--white);font-family:var(--serif);font-weight:600;font-size:25px}
.service-icon{width:76px;height:76px;margin:0 auto 16px;background:var(--rose-soft)}
.services .btn{background:var(--white);color:var(--rose);left:534px;top:346px;width:132px;height:46px}

/* blog */
.post{position:absolute;top:2788px;width:311px;text-align:center}
.post .photo{position:relative;width:311px;height:234px}
.post h3{margin-top:28px;font-family:var(--serif);font-weight:600;font-size:23px;color:var(--ink)}
.post p{margin-top:14px;font-size:13.5px;line-height:29px;padding:0 8px}

/* cta */
.cta{position:absolute;left:0;top:3236px;width:1200px;height:396px;background:linear-gradient(180deg,#66676a,var(--cta))}
.cta h2{position:absolute;left:0;top:110px;width:1200px;text-align:center;font-family:var(--serif);font-weight:600;font-size:52px;line-height:56px;color:var(--white)}

/* footer */
.footer h2{position:absolute;font-family:var(--serif);font-weight:600;font-size:42px;color:var(--ink)}
.footer p{position:absolute;font-size:17px;line-height:31px;color:var(--ink)}
.footer .link{position:absolute;font-size:18px;color:var(--rose)}
.social{position:absolute;left:512px;top:3810px;display:flex;gap:14px}
.social span{width:16px;height:16px;border-radius:50%;background:var(--ink)}
</style>
</head>
<body>

<header class="hero">
  <div class="photo" role="img" aria-label="City street with tall stone office buildings and a lit street lamp at dusk" style="inset:0;background:linear-gradient(160deg,#57504b,#3b3734 55%,#7a6c62)"></div>
  <div class="hero-shade"></div>
  <div class="brand"><span class="brand-mark"></span><span class="brand-name">Hollinbrook Counsel</span></div>
  <nav class="nav"><a class="active" href="#">Home</a><a href="#">Services</a><a href="#">Research</a><a href="#">The Institute</a><a href="#">In the News</a></nav>
  <a class="btn" href="#" style="left:955px;top:22px;width:132px;height:46px">Contact Us</a>
  <h1>Macroeconomic &amp; policy analytics for today’s turbulent environment.</h1>
  <p>The Hollinbrook Policy Institute (HPI) is an independent non-profit organization that partners with private think tanks, academic macroeconomic policy concerns of today.</p>
  <a class="btn" href="#" style="left:109px;top:444px;width:132px;height:46px">Contact Us</a>
</header>

<section class="about">
  <h2 class="title" style="top:672px">About Us</h2>
  <p class="center-copy" style="top:747px">The Hollinbrook Policy Institute (HPI) is an independent non-profit organization that partners with private think tanks, academic institutions, and policy advocacy organizations to develop unbiased investigations and reasoned responses to the macroeconomic policy concerns of today.</p>
  <p class="center-copy" style="top:874px">Please see below for a growing list of current partners, support organizations, and affiliated institutions, along with a preview of some of our recent work.</p>
  <a class="btn" href="#" style="left:534px;top:964px;width:132px;height:46px">Read More</a>
</section>

<section class="feature">
  <div class="photo" role="img" aria-label="Tablet resting on printed financial charts with a line graph" style="left:111px;top:1087px;width:446px;height:462px;background:linear-gradient(135deg,#8aa6c4,#dfe6ee 50%,#b9c8d8)"></div>
  <h2 style="left:607px;top:1110px;width:540px">Sophisticated research &amp;<br>atypical analyses for<br>improved communications.</h2>
  <p style="left:607px;top:1274px;width:480px">The Hollinbrook Policy Institute (HPI) is an independent non-profit organization that partners with private think tanks, academic institutions, and policy advocacy organizations to develop unbiased investigations and reasoned responses to the macroeconomic policy concerns of today. Please see below for a growing list of current partners, support organizations, and affiliated institutions, along with a preview of some of our recent work.</p>
  <a class="mail" href="#" style="left:606px;top:1497px">info@HollinbrookCounsel.com</a>
</section>

<section class="feature">
  <h2 style="left:110px;top:1650px;width:500px">Proprietary public<br>relations tools that<br>guarantee media visibility</h2>
  <p style="left:110px;top:1814px;width:480px">The Hollinbrook Policy Institute (HPI) is an independent non-profit organization that partners with private think tanks, academic institutions, and policy advocacy organizations to develop unbiased investigations and reasoned responses to the macroeconomic policy concerns of today. Please see below for a growing list of current partners, support organizations, and affiliated institutions, along with a preview of some of our recent work.</p>
  <a class="mail" href="#" style="left:109px;top:2037px">info@HollinbrookCounsel.com</a>
  <div class="photo" role="img" aria-label="Close-up of stacked folded newspapers in cool blue light" style="left:643px;top:1627px;width:446px;height:462px;background:linear-gradient(135deg,#6f8eb2,#c8d5e2 55%,#e6ecf2)"></div>
</section>

<section class="services">
  <h2 class="title">Our Services</h2>
  <div class="service" style="left:105px">
    <div class="service-icon" role="img" aria-label="Analytics and messaging icon"></div>
    Analytics &amp; Messaging
  </div>
  <div class="service" style="left:442px">
    <div class="service-icon" role="img" aria-label="Customized reports icon"></div>
    Customized Reports
  </div>
  <div class="service" style="left:767px">
    <div class="service-icon" role="img" aria-label="Proprietary surveys icon"></div>
    Proprietary Surveys
  </div>
  <a class="btn" href="#">View More</a>
</section>

<section class="blog">
  <h2 class="title" style="top:2712px">Our Blog</h2>
  <article class="post" style="left:113px">
    <div class="photo" role="img" aria-label="Laptop on a desk displaying an analytics dashboard" style="background:linear-gradient(160deg,#2f3640,#6d7783 60%,#a7b0b8)"></div>
    <h3>Analytics &amp; Messaging</h3>
    <p>Our communications team can develop influential messaging, in conjunction with our data scientists’ technical expertise.</p>
  </article>
  <article class="post" style="left:444px">
    <div class="photo" role="img" aria-label="Hands turning the pages of a printed report" style="background:linear-gradient(160deg,#2b2725,#5e5650 55%,#9a8f86)"></div>
    <h3>Customized Reports</h3>
    <p>From succinct summations of economic and policy impact to full-length analyses, we can create the represents your interests.</p>
  </article>
  <article class="post" style="left:776px">
    <div class="photo" role="img" aria-label="Colleagues reviewing survey results on a tablet beside a laptop" style="background:linear-gradient(160deg,#b9a585,#e2d8c6 50%,#4f5f73)"></div>
    <h3>Proprietary Surveys</h3>
    <p>Exclusive, custom-designed surveys can enrich your databank, while maintaining access to proprietary resources</p>
  </article>
</section>

<section class="cta">
  <div class="photo" role="img" aria-label="Hazy city skyline with skyscrapers under a grey sky" style="inset:0;background:linear-gradient(180deg,#707175,#595a5e 60%,#4c4d50)"></div>
  <h2>Proprietary public relations tools<br>that guarantee media visibility.</h2>
  <a class="btn" href="#" style="left:534px;top:255px;width:132px;height:46px">Read More</a>
</section>

<footer class="footer">
  <h2 style="left:109px;top:3688px">Stay in touch.</h2>
  <p style="left:109px;top:3763px;width:340px">418 Alder Row, Suite 210, Easton, MD 21601</p>
  <h2 style="left:512px;top:3688px">Quick Links</h2>
  <p style="left:512px;top:3763px">Contact Us</p>
  <div class="social" aria-label="Social links"><span></span><span></span></div>
  <a class="link" href="#" style="left:799px;top:3700px">Home</a>
  <a class="link" href="#" style="left:799px;top:3756px">Services</a>
  <a class="link" href="#" style="left:799px;top:3812px">Research</a>
  <a class="link" href="#" style="left:971px;top:3700px">The Institute</a>
  <a class="link" href="#" style="left:971px;top:3756px">In the News</a>
  <a class="link" href="#" style="left:971px;top:3812px">Contact</a>
  <p style="left:110px;top:3857px">©2024.Company Name.All Rights Reserved</p>
</footer>

</body>
</html>
```